Poster Needed for Church Conference

I need a poster for a weekend conference at my church. Looking to attract as many people as possible. We are a church in the suburbs of Houston. This is mainly for our own church members but we are opening it up to outside church members.

Please see previous design from last conference and all other graphic work that can (doesn't need to be) included.

Target Market(s)

It's targeted for all people. But our main audience is families. around the age of 30 should be main target.

Industry/Entity Type

Non-Profit

Font styles to use
Serif
Sans Serif

Colors

Designer to choose colors to be used in the design.

Requirements
Must have
• 11x17 design with ability to shrink and blow up. but ideally for 11x17
• Content and wording:
• "Rooted Light Conference: Bridging the gap between generations and passing on our deepest beliefs and values."
• Featuring Dr. Gil Marsden. Author of "The Path of P4"
• Aug 25-26: Friday 8-10 pm, Saturday 4-8 pm
• Cost Adults $15/Children $5: Covers admission to all sessions and workshops, refreshments and Saturday dinner. *kids 5 and under free
• Childcare provided for all sessions. "
• Please use church logo and address on flyer: 4312 Route 19, Missouri City, TX 77988
Nice to have
• Ideally it will be designed so that we can crop a 16:9 pp announcement slide and header for our website.
Should not have
• anything offensive

```html
<!DOCTYPE html>
<html lang="en">
<head>
<meta charset="UTF-8">
<title>Rooted Light Conference</title>
<link href="https://fonts.googleapis.com/css2?family=Source+Sans+3:wght@400;600;700;900&display=swap" rel="stylesheet">
<style>
  :root {
    --ink: #151515;
    --ink-soft: #2b2b2b;
    --white: #ffffff;
    --green: #6abd2b;
    --green-deep: #5aab1f;
    --blue: #1b5ea6;
    --photo-warm: #c8a78a;
    --photo-light: #eadccb;
    --photo-navy: #1f2740;
  }
  * { box-sizing: border-box; margin: 0; padding: 0; }
  html, body { width: 1200px; height: 776px; overflow: hidden; background: var(--white); }
  body { font-family: "Source Sans 3", sans-serif; color: var(--ink); }

  .poster { position: relative; width: 1200px; height: 776px; overflow: hidden; background: var(--white); }

  .poster__photo {
    position: absolute; left: 0; top: 0; width: 820px; height: 776px;
    background:
      radial-gradient(ellipse 320px 220px at 180px 700px, rgba(31,39,64,0.85), rgba(31,39,64,0) 100%),
      radial-gradient(ellipse 260px 300px at 430px 260px, rgba(200,167,138,0.9), rgba(200,167,138,0) 100%),
      linear-gradient(90deg, var(--photo-warm) 0%, var(--photo-light) 55%, rgba(255,255,255,0) 100%);
  }

  .poster__band {
    position: absolute; left: 420px; top: 340px; width: 780px; height: 282px;
    background: linear-gradient(90deg, rgba(106,189,43,0) 0%, rgba(106,189,43,0.85) 22%, var(--green) 34%, var(--green) 100%);
  }

  .title {
    position: absolute; right: 44px; top: 28px; text-align: right;
    font-weight: 900; font-size: 82px; line-height: 0.96; letter-spacing: 0.5px;
    text-transform: uppercase; color: var(--ink);
  }
  .tagline {
    position: absolute; right: 44px; top: 192px; width: 560px; text-align: center;
    font-size: 24px; line-height: 1.2; color: var(--ink-soft);
  }
  .featuring {
    position: absolute; left: 600px; width: 554px; text-align: center; top: 274px;
    font-weight: 700; font-size: 16px; letter-spacing: 0.3px; color: var(--ink);
  }
  .speaker {
    position: absolute; left: 600px; width: 554px; text-align: center; top: 300px;
    font-weight: 700; font-size: 23px; color: var(--blue);
  }

  .details { position: absolute; left: 600px; width: 554px; top: 352px; text-align: center; color: var(--white); }
  .details__date { font-weight: 700; font-size: 54px; line-height: 1; }
  .details__times { font-weight: 700; font-size: 30px; margin-top: 12px; }
  .details__cost-label { font-weight: 700; font-size: 25px; color: var(--ink); margin-top: 12px; }
  .details__price { font-size: 21px; color: var(--ink); margin-top: 4px; }
  .details__note { font-size: 15px; line-height: 1.3; color: var(--ink); margin-top: 6px; }
  .details__childcare { font-size: 15.5px; color: var(--ink); margin-top: 10px; }

  .church {
    position: absolute; right: 46px; top: 652px; display: flex; align-items: center; gap: 14px;
    color: var(--green-deep); font-weight: 600;
  }
  .church__dot { width: 34px; height: 34px; border-radius: 50%; background: var(--green-deep); }
  .church__name { font-size: 30px; line-height: 1; letter-spacing: 1px; }

  .address {
    position: absolute; right: 46px; top: 731px; font-size: 16px; color: var(--ink);
  }
</style>
</head>
<body>
<main class="poster">
  <div class="poster__photo" role="img" aria-label="Photo of a grandfather and a young child playing together with a toy train"></div>
  <div class="poster__band"></div>

  <h1 class="title">Rooted Light<br>Conference</h1>
  <p class="tagline">Bridging the gap between generations and passing on our deepest beliefs and values.</p>

  <p class="featuring">FEATURING</p>
  <p class="speaker">Dr. Gil Marsden. Author of "The Path of P4"</p>

  <section class="details">
    <p class="details__date">Aug 25-26</p>
    <p class="details__times">Friday 8-10 pm, Saturday 4-8 pm</p>
    <p class="details__cost-label">Cost</p>
    <p class="details__price">Adults $15/Children $5</p>
    <p class="details__note">Covers admission to all sessions and workshops,<br>refreshments and Saturday dinner. *kids 5 and under free</p>
    <p class="details__childcare">Childcare provided for all sessions.</p>
  </section>

  <div class="church">
    <span class="church__dot"></span>
    <span class="church__name">Cedar Hollow Community Church</span>
  </div>
  <p class="address">4312 Route 19, Missouri City, TX 77988</p>
</main>
</body>
</html>
```